Rug Cleaning Web Design Project

We need a web design for our cleaning company. We currently have a web page but are not happy with its design. We currently offer fine rug cleaning,upholstery cleaning, and residential and commercial carpet cleanning. We also offer water damage restoration. For our rug cleaning services we offer : Enzyme treatments for pet contamination and odor removal, application of stain protection that is designed for the fine textiles used in rug construction, application of treatments designed to prevent moth damage and pads designed to be used under rugs.Our current web site is harborlinewash.example. We are intrested in a design with similar information to the web page of Velmora Rug Cleaners INC. We would like to use the colors that are present in our logo that will be uploaded with this description. We would also like this new page to be linked to our other address fibertendpro.example. We would like the deign to be visually attractive but not "too busy".
Updates

Please include pictures of rugs, or people washing rugs if possible. We do not offer maid type cleaning services. We would not be interested in designs including pictures depicting that type service. Thanks for your hard work on this project.

Dale Hutchins

Industry/Entity Type

Residential

Requirements
Must have
• This page must be viewable on smart phones and tablets.

```html
<!DOCTYPE html>
<html lang="en">
<head>
<meta charset="utf-8">
<meta name="viewport" content="width=device-width, initial-scale=1">
<title>FiberTend Pro — Harborline Cleaning, LLC</title>
<link rel="stylesheet" href="https://fonts.googleapis.com/css2?family=Arimo:wght@400;700&family=Roboto+Condensed:wght@400&family=PT+Sans:wght@400;700&display=swap">
<style>
:root{
  --sky:#84bfe4;
  --white:#ffffff;
  --paper:#f6f6f6;
  --ink:#222222;
  --heading:#3b3b3b;
  --muted:#7a7a7a;
  --brand:#2f6fb3;
  --green:#3aa524;
  --green-dark:#1f7d12;
  --footer:#4b4b4b;
  --caption:rgba(70,66,62,.82);
}
*{box-sizing:border-box;margin:0;padding:0}
html,body{width:1200px;height:1026px;overflow:hidden}
body{position:relative;background:var(--white);font-family:"Arimo",Arial,sans-serif;color:var(--ink)}
.abs{position:absolute}

.site-header{left:0;top:0;width:1200px;height:112px;background:var(--white);box-shadow:0 2px 6px rgba(0,0,0,.18);z-index:2}
.brand{left:148px;top:34px;display:flex;align-items:center;gap:12px}
.brand-mark{width:40px;height:40px;border-radius:50%;background:var(--brand)}
.brand-name{font-weight:700;font-size:33px;color:#333;letter-spacing:-1px;line-height:1}
.brand-sub{font-size:11.5px;letter-spacing:3px;color:#555;margin-top:3px}
.main-nav{left:534px;top:0;height:112px;display:flex}
.main-nav a{display:flex;align-items:center;justify-content:center;height:112px;font-size:16px;color:var(--ink);text-decoration:none;border-left:1px solid #eee;box-shadow:-4px 0 6px -4px rgba(0,0,0,.15)}
.main-nav a:last-child{border-right:1px solid #eee}

.hero{left:0;top:112px;width:1200px;height:436px;background:var(--sky)}
.slider-frame{left:148px;top:141px;width:899px;height:379px;background:var(--white);border:1px solid #d8d8d8;border-radius:4px}
.slide-photo{left:164px;top:153px;width:870px;height:346px;border-radius:8px;background:linear-gradient(160deg,#a29284 0%,#cdc2b8 35%,#d9d0c8 60%,#b7aaa0 100%)}
.slide-caption{left:164px;top:338px;width:506px;height:127px;background:var(--caption);color:var(--white);padding:17px 20px 0 36px}
.slide-caption h2{font-weight:400;font-size:19.5px;margin-bottom:9px}
.slide-caption p{font-size:13.4px;line-height:19.7px}
.slider-arrow{top:288px;width:29px;height:60px;background:linear-gradient(var(--green),var(--green-dark));border-radius:2px;display:flex;align-items:center;justify-content:center}

.features{left:0;top:548px;width:1200px;height:185px;background:var(--paper)}
.feature{top:574px;width:290px}
.feature-head{display:flex;align-items:center;gap:10px;height:38px}
.feature-icon{width:36px;height:36px;flex:none}
.feature h3{font-family:"Roboto Condensed","Arial Narrow",sans-serif;font-weight:400;font-size:21.5px;color:var(--heading)}
.feature p{margin-top:12px;font-size:11.6px;line-height:18.75px;color:var(--muted)}

.info{left:0;top:733px;width:1200px;height:236px;background:var(--sky)}
.info-col{top:757px;color:var(--white)}
.info-col h4{font-family:"PT Sans",Arial,sans-serif;font-weight:400;font-size:19px;margin-bottom:12px}
.divider{top:757px;width:1px;height:182px;background:rgba(255,255,255,.4)}
.tweet{font-size:12.4px;line-height:17.8px;padding-left:2px}
.tweet b{font-weight:700}
.tweet small{display:block;font-size:11.8px}
.tweet-sep{border-top:1px dashed rgba(255,255,255,.8);margin:9px 0 11px;width:270px}
.news p{font-size:12.6px;line-height:18px;width:280px}
.email-field{margin-top:12px;width:261px;height:32px;border:1px solid #ccc;border-radius:3px;background:var(--white);font-style:italic;font-size:11.5px;color:#aaa;padding:8px 9px}
.subscribe{margin-top:12px;width:132px;height:31px;border-radius:4px;background:linear-gradient(#38a828,#138b0c);border:1px solid #0e6d08;color:var(--white);font-size:11.5px;display:flex;align-items:center;justify-content:center;font-family:"PT Sans",Arial,sans-serif}
.contact-row{display:flex;gap:14px;align-items:flex-start;margin-bottom:10px;font-size:11.8px;line-height:19px}
.contact-icon{width:32px;height:32px;border-radius:50%;background:linear-gradient(#f4f4f4,#cfcfcf);display:flex;align-items:center;justify-content:center;margin-left:9px;flex:none}

.bottom-bar{left:0;top:969px;width:1200px;height:57px;background:var(--footer)}
.social{top:981px;width:32px;height:32px;border-radius:4px}
.bottom-links{right:151px;top:981px;text-align:right;color:var(--white);font-size:11.8px;line-height:17.5px}
</style>
</head>
<body>

<header class="abs site-header">
  <div class="abs brand">
    <div class="brand-mark"></div>
    <div>
      <div class="brand-name">FiberTend Pro</div>
      <div class="brand-sub">HARBORLINE CLEANING, LLC</div>
    </div>
  </div>
  <nav class="abs main-nav">
    <a href="#" style="width:103px">HOME</a>
    <a href="#" style="width:131px">ABOUT US</a>
    <a href="#" style="width:127px">SERVICES</a>
    <a href="#" style="width:150px">CONTACT US</a>
  </nav>
</header>

<section class="abs hero"></section>
<div class="abs slider-frame"></div>
<div class="abs slide-photo" role="img" aria-label="Photo of a carpet cleaning wand gliding over a freshly cleaned beige carpet"></div>
<div class="abs slide-caption">
  <h2>Carpet &amp; Upholstery Cleaning</h2>
  <p>Wool or synthetic, woven or tufted, residential or commercial, the experienced technicians at Harborline know how to restore your carpet's appearance... and to provide you with a healthier indoor enviroment.</p>
</div>
<div class="abs slider-arrow" style="left:142px">
  <svg width="12" height="18" viewBox="0 0 12 18"><path d="M9 2 L3 9 L9 16" stroke="#fff" stroke-width="3" fill="none"/></svg>
</div>
<div class="abs slider-arrow" style="left:1026px">
  <svg width="12" height="18" viewBox="0 0 12 18"><path d="M3 2 L9 9 L3 16" stroke="#fff" stroke-width="3" fill="none"/></svg>
</div>

<section class="abs features"></section>
<div class="abs feature" style="left:147px">
  <div class="feature-head">
    <div class="feature-icon" role="img" aria-label="Magic wand with stars icon" style="background:linear-gradient(135deg,#f2c230,#555);border-radius:4px"></div>
    <h3>GUARANTEE SERVICES</h3>
  </div>
  <p>Lorem ipsum dolor sit amet, consectetur adipisicing elit, sed do eiusmod tempor incididunt ut labore et dolore magna aliqua. Ut enim ad minim veniam, quis nostrud exercitation ullamco laboris nisi ut aliquip ex ea.</p>
</div>
<div class="abs feature" style="left:459px">
  <div class="feature-head">
    <div class="feature-icon" role="img" aria-label="Staff member portrait icon" style="background:linear-gradient(#c99a7a,#3c4e6e);border-radius:4px"></div>
    <h3>PROFESSIONAL STAFFS</h3>
  </div>
  <p>Lorem ipsum dolor sit amet, consectetur adipisicing elit, sed do eiusmod tempor incididunt ut labore et dolore magna aliqua. Ut enim ad minim veniam, quis nostrud exercitation ullamco laboris nisi ut aliquip ex ea.</p>
</div>
<div class="abs feature" style="left:766px">
  <div class="feature-head">
    <svg class="feature-icon" viewBox="0 0 36 36" aria-hidden="true"><circle cx="18" cy="18" r="17" fill="#f2b51e"/><circle cx="18" cy="18" r="12.5" fill="#fff"/><path d="M18 9 V18 L23 22" stroke="#777" stroke-width="2" fill="none"/></svg>
    <h3>ALWAYS BE ON TIME</h3>
  </div>
  <p>Lorem ipsum dolor sit amet, consectetur adipisicing elit, sed do eiusmod tempor incididunt ut labore et dolore magna aliqua. Ut enim ad minim veniam, quis nostrud exercitation ullamco laboris nisi ut aliquip ex ea.</p>
</div>

<section class="abs info"></section>
<div class="abs divider" style="left:440px"></div>
<div class="abs divider" style="left:745px"></div>

<div class="abs info-col" style="left:148px;width:282px">
  <h4>Recent Social Update</h4>
  <p class="tweet"><b>@client</b> lorem ipsum dolor sit amet, consectetur elit, sed do eiusmod tempor incididunt ut labore et dolore magna aliqua. Ut enim ad minim veniam<small>12 minutes ago</small></p>
  <div class="tweet-sep"></div>
  <p class="tweet"><b>@client</b> lorem ipsum dolor sit amet, consectetur elit, sed do eiusmod tempor incididunt iam<small>12 minutes ago</small></p>
</div>

<div class="abs info-col news" style="left:460px">
  <h4>Newsletter</h4>
  <p>Subscribe our newsletter and get connected with our new product</p>
  <div class="email-field">enter your email address</div>
  <div class="subscribe">SUBSCRIBE</div>
</div>

<div class="abs info-col" style="left:767px">
  <h4>Contact Us</h4>
  <div class="contact-row">
    <div class="contact-icon"><svg width="16" height="16" viewBox="0 0 16 16"><path d="M4 1 L6 5 L5 6.5 Q7 10 9.5 11 L11 10 L15 12 L13.5 15 Q6 14.5 1.5 3 Z" fill="#9a9a9a"/></svg></div>
    <div>+1 (555) 01.24.680<br>+1 (555) 01.24.680</div>
  </div>
  <div class="contact-row">
    <div class="contact-icon"><svg width="16" height="12" viewBox="0 0 16 12"><rect x="0.5" y="0.5" width="15" height="11" fill="#9a9a9a"/><path d="M1 1 L8 7 L15 1" stroke="#eee" stroke-width="1.3" fill="none"/></svg></div>
    <div>hello@harborlinewash.example<br>service@harborlinewash.example</div>
  </div>
  <div class="contact-row">
    <div class="contact-icon"><svg width="16" height="15" viewBox="0 0 16 15"><path d="M8 1 L15 7.5 H13 V14 H9.5 V10 H6.5 V14 H3 V7.5 H1 Z" fill="#9a9a9a"/></svg></div>
    <div>48 Tidewater Lane,<br>Port Elmridge, 60412, U.S.A.</div>
  </div>
</div>

<footer class="abs bottom-bar"></footer>
<div class="abs social" style="left:148px;background:#8cc7d6"></div>
<div class="abs social" style="left:194px;background:#4f6fa8"></div>
<div class="abs social" style="left:240px;background:#f08a24"></div>
<div class="abs bottom-links">
  Home &nbsp;|&nbsp; About Us &nbsp;|&nbsp; Product &nbsp;|&nbsp; Contact Us<br>
  © 2012 Harborline Cleaning All Rights Reserved.
</div>

</body>
</html>
```